Printed Circuit Board Company Web Site Design - Please see new file 82012 web design

We are a printed circuit board manufacturer. Need a company professional web site to allow our potential customers to know more about our background, capability and our products. The web site will contain three languages, which are Chinese, English and Japanese. Our audience are mainly electronic companies that procure printed circuit boards. I have a word document that have all the required text in all three languages. The final design should communicate the impression that we embrace quality, trustworthiness and long term partnership business principles.
We should have sections that allow us to post pictures of our facilities.
I have added the three files in three different languages.
Some of the information is below:
Background
RVT Global Limited (RVT) was set up in Hong Kong in 2007 by two Hong Kong entrepreneurs, Mr. Lau Fong and Mr. Tak Wai. We acquired the single sided printed circuit board factory located in Dongguan City, Guangdong Province, China, from Bolvane Corporation of the U.S. in 2007. In addition to RVT, Mr. Fong and Mr. Wai also own Harbor Dynamics Company Limited, a semiconductor company based in Hong Kong since 1997 with a total investment of over US$100 million. Harbor is engaged in the manufacturing of flexible substrates and MEMS assembly business.
RVT has been awarded TS 16949 and ISO14000 certificates since 2009 and 2004 respectively.
Business Principles
RVT Global Limited strives to be a professional top notched printed circuit board supplier. We embrace four “EXCELLENCE” principles, namely, excellence in quality, excellence in prices, excellence in services and excellence in on time delivery.
We approach each customer with a long-term partnership view that delivers the lowest ownership costs and highest total values to our customers. We customize quotations and solutions in order to allow our customers to win more businesses. We believe by thinking from our customers’ points of view we will be able to create a WIN-WIN relationship.
Customers
Due to our excellent quality, services and production systems, RVT Global Limited manage to service a number of large Japanese and US customers, which include:
Technical capability overview
Below is an overview of our current capability:
Target Market(s)
Electronic companies buyers
Industry/Entity Type
Business
Requirements
Must have
- Capability description
Should not have
- no cartoon

```html
<!DOCTYPE html>
<html lang="en">
<head>
<meta charset="utf-8">
<title>RVT Global Limited</title>
<link rel="stylesheet" href="https://fonts.googleapis.com/css2?family=Carlito:wght@400;700&family=Bree+Serif&family=Arimo:wght@400;700&display=swap">
<style>
:root{
  --green:#0f7a55;
  --green-dark:#1c5a3e;
  --footer:#1f5f42;
  --footer-text:#8fd9a8;
  --red:#d42a1c;
  --blue:#3e6fb4;
  --blue-light:#6e9bd6;
  --text:#333;
  --grey-panel:#ececec;
  --gold:#e5a90c;
  --yellow:#f4c61e;
}
*{box-sizing:border-box;margin:0;padding:0}
html,body{width:821px;height:1200px;overflow:hidden}
body{position:relative;font-family:'Carlito',Calibri,sans-serif;color:var(--text);background:#fff}
.abs{position:absolute}
.top-band{left:0;top:0;width:821px;height:287px;background:linear-gradient(#fff 0,#f6f8f7 60px,#dfe8e3 150px,#a9c6b6 215px,#3f8465 260px,#2e7458 287px)}
.brand{left:96px;top:14px;width:116px;color:var(--green);font-weight:700;font-size:17px;line-height:17px;text-align:center}
.brand .mark{display:block;font-size:30px;line-height:26px;letter-spacing:2px}
.brand .sub{font-size:11px;line-height:12px}
.lang{left:461px;top:18px;font-size:9px;font-family:'Arimo',Arial,sans-serif;color:#222;display:flex;align-items:center;gap:4px}
.lang .pill{width:56px;height:13px;border-radius:7px;background:linear-gradient(#fff,#dcdcdc);border:1px solid #aaa;position:relative;font-size:8px;padding-left:4px;line-height:11px}
.lang .pill i{position:absolute;right:-1px;top:-1px;width:15px;height:13px;border-radius:0 7px 7px 0;background:#2f9a5c}
.call{left:607px;top:16px;font-size:11px;color:#222}
.call b{display:block;font-weight:400;font-size:17px;color:var(--red);font-family:'Arimo',Arial,sans-serif;margin-top:3px}
.nav{left:96px;top:69px;width:629px;height:28px;border-radius:8px 8px 0 0;background:linear-gradient(#6f9ad5,#3b6bb2);display:flex;font-family:'Arimo',Arial,sans-serif;font-size:10.5px;color:#fff}
.nav a{color:#fff;text-decoration:none;display:flex;align-items:center;justify-content:center;border-right:1px solid #5a86c4;height:100%}
.hero{left:96px;top:96px;width:629px;height:213px;border:1px solid #a9bfd8;border-top:0;border-radius:0 0 10px 10px;overflow:hidden;background:radial-gradient(circle at 530px 90px,#fff 0,#e7eef6 120px,#d5e1ee 250px)}
.hero-photo{left:0;top:0;width:386px;height:213px;clip-path:polygon(0 0,372px 0,386px 213px,0 213px);background:linear-gradient(135deg,#8d8a83,#c9c4b6 35%,#5f7c4a 60%,#2f5a2e 85%,#3b3b38)}
.hero-edge{left:372px;top:0;width:15px;height:213px}
.hero-caption{left:0;top:182px;width:383px;height:31px;background:rgba(60,88,120,.85);color:#fff;font-family:'Arimo',Arial,sans-serif;font-weight:700;font-size:16px;padding:5px 0 0 19px}
.hero-title{right:13px;top:42px;font-family:'Bree Serif',serif;font-size:16.5px;line-height:19px;color:#333;text-align:right}
.hero-title em{font-style:normal;color:var(--red)}
.hero-text{right:13px;top:104px;width:225px;text-align:right;font-family:'Arimo',Arial,sans-serif;font-size:9.5px;line-height:13px;color:#222}
.hero-btn{left:454px;top:163px;width:109px;height:24px;border-radius:4px;background:linear-gradient(#f7d45a,var(--gold));border:1px solid #b78406;font-family:'Arimo',Arial,sans-serif;font-size:10px;color:#222;text-align:center;line-height:22px}
h2{font-weight:400;font-size:16px;color:#222}
h2 .accent{color:var(--red)}
.copy{font-size:8.6px;line-height:15.2px;color:#333}
.more{font-size:9px;font-style:italic;color:var(--red);text-align:right}
.more::before{content:"\2295 ";font-style:normal;font-size:8px}
.rule{height:1px;background:linear-gradient(90deg,transparent,#d0d0d0 30%,#d0d0d0 70%,transparent)}
.thumb{border:1px solid #ccc;background:#fff;padding:3px;box-shadow:0 1px 2px rgba(0,0,0,.15)}
.thumb div{width:100%;height:100%}
.products{left:96px;top:668px;width:427px;height:164px;background:#f1f1f1;border-radius:3px}
.product-title{font-size:11px;color:var(--green-dark)}
.clients{left:96px;top:873px;width:427px;height:85px;background:linear-gradient(#fff,#f2f2f2);border:1px solid #ddd;box-shadow:0 6px 6px -5px rgba(0,0,0,.3)}
.client{top:13px;width:68px;height:57px;border:1px solid #ccc;background:#fff;box-shadow:0 1px 3px rgba(0,0,0,.2);display:flex;align-items:center;justify-content:center;font-weight:700;font-size:11px;text-align:center}
.side-head{left:560px;width:165px;height:27px;color:#fff;font-size:15px;padding:4px 0 0 13px}
.side-head.green{background:linear-gradient(#2a9b6e,#0d6a48)}
.side-head.grey{background:linear-gradient(#8b8b85,#5c5c57)}
.side-body{left:560px;width:165px;background:var(--grey-panel);border-bottom:2px solid #e8d7b3}
.cap-list{list-style:none;padding:4px 11px 0 12px}
.cap-list li{height:23px;line-height:23px;font-size:9.5px;color:#222;border-bottom:1px solid #dcdcdc}
.cap-list li:last-child{border-bottom:0}
.cap-list li::before{content:"\2022";margin-right:5px;font-size:8px}
.bubble{left:7px;top:8px;width:151px;height:104px;background:#fff;border-radius:10px;box-shadow:0 1px 3px rgba(0,0,0,.25);font-style:italic;font-size:9.5px;line-height:14px;padding:16px 12px 0 13px;color:#444}
.blog-item{left:12px;width:150px}
.blog-item h4{font-weight:400;font-size:11px;color:var(--red);padding-left:15px}
.blog-item p{font-size:8.4px;line-height:14px;padding-left:15px;color:#333}
.blog-item svg{position:absolute;left:0;top:2px}
.btn-view{left:107px;top:166px;width:45px;height:17px;border-radius:3px;background:linear-gradient(var(--blue-light),#2f5d9f);color:#fff;font-size:9px;text-align:center;line-height:17px;font-weight:700}
.footer{left:0;top:977px;width:821px;height:223px;background:repeating-linear-gradient(0deg,rgba(255,255,255,.015) 0 2px,rgba(0,0,0,.02) 2px 4px),var(--footer)}
.footer h3{position:absolute;font-weight:400;font-size:17px;color:#fff}
.f-col{font-size:9px;line-height:14.2px;color:var(--footer-text)}
.f-col .label{color:#fff;font-size:9.5px}
.f-col .white{color:#fff;font-size:9.5px}
.f-col .white u{color:#fff}
.f-phone{font-family:'Arimo',Arial,sans-serif;font-weight:700;color:var(--yellow);font-size:13px}
.f-links{list-style:none;font-size:8.5px;line-height:15.4px;color:var(--footer-text)}
.social{left:615px;width:110px;height:26px;border-radius:3px;background:rgba(255,255,255,.08);border:1px solid rgba(255,255,255,.08);font-size:8.5px;color:var(--footer-text);display:flex;align-items:center;gap:7px;padding-left:6px}
.social i{width:18px;height:18px;border-radius:2px;display:block}
.copyright{font-size:9.5px;color:var(--footer-text)}
</style>
</head>
<body>
<div class="abs top-band"></div>

<header>
  <div class="abs brand"><span class="mark">RVT</span><span class="sub">Global Limited</span></div>
  <div class="abs lang">Select Language: <span class="pill">English<i></i></span></div>
  <div class="abs call">Call Us Now!<b>(852)21904468</b></div>
  <nav class="abs nav">
    <a style="width:68px">Home</a>
    <a style="width:81px">About us</a>
    <a style="width:79px">Products</a>
    <a style="width:79px">Services</a>
    <a style="width:128px">Technical capability</a>
    <a style="width:102px">Infrastructure</a>
    <a style="width:92px;border-right:0">Our Clients</a>
  </nav>
</header>

<section class="abs hero">
  <div class="abs hero-photo" role="img" aria-label="Engineer testing a printed circuit board with an oscilloscope and multimeter"></div>
  <svg class="abs hero-edge" width="15" height="213" viewBox="0 0 15 213"><line x1="0.5" y1="0" x2="14" y2="213" stroke="#e8731f" stroke-width="2"/></svg>
  <div class="abs hero-caption">Lorem ipsum dolor sit amet...</div>
  <div class="abs hero-title"><em>Neque porro</em> quisquam est<br>dolorem ipsum dolor sit amet...</div>
  <p class="abs hero-text">Neque porro quisquam est qui dolorem ipsum quia dolor sit amet, consectetur, adipisci velit there is no one who loves pain itself.</p>
  <div class="abs hero-btn">Click for Capability</div>
</section>

<main>
  <h2 class="abs" style="left:96px;top:325px">Welcome to <span class="accent">RVT Global Limited</span></h2>
  <p class="abs copy" style="left:96px;top:348px;width:428px">Lorem Ipsum is simply dummy text of the printing and typesetting industry. Lorem Ipsum has been the industry's for on standard dummy text ever since the 1500s, when an unknown printer took a galley of type and scrambled it to make a passages, and more recently with desktop publishing.</p>
  <p class="abs copy" style="left:96px;top:400px;width:428px">Lorem Ipsum is simply dummy text of the printing and typesetting industry. Lorem Ipsum has been the industry's &nbsp;into standard dummy text ever since the 1500s, when an unknown printer took a galley of type and scrambled it to make a type specimen book. It has survived not only five centuries, but also the leap into electronic typesetting, remaining go essentially unchanged. It was popularised in the 1960s with the release of Letraset sheets containing lorem Ipsum play type specimen book. It has survived not only five centuries, but also the leap into electronic typesetting.</p>
  <div class="abs more" style="left:440px;top:484px;width:82px">Read More</div>
  <div class="abs rule" style="left:96px;top:505px;width:428px"></div>

  <h2 class="abs" style="left:96px;top:517px">Our Services</h2>
  <div class="abs thumb" style="left:96px;top:544px;width:79px;height:53px"><div role="img" aria-label="Technician working on a circuit board" style="background:linear-gradient(135deg,#7aa0b8,#c7b8a5 50%,#3d6c9a)"></div></div>
  <p class="abs copy" style="left:186px;top:540px;width:338px">Lorem Ipsum is simply dummy text of the printing and typesetting industry. Lorem Ipsum has been the industry's for on standard dummy text ever since the 1500s, when an unknown printer took a galley of type and scrambled it to make a passages, and more recently with desktop publishing centuries.</p>
  <div class="abs more" style="left:440px;top:608px;width:82px">Read More</div>
  <div class="abs rule" style="left:96px;top:629px;width:428px"></div>

  <h2 class="abs" style="left:95px;top:640px">Products</h2>
  <div class="abs products">
    <div class="abs thumb" style="left:6px;top:6px;width:202px;height:92px"><div role="img" aria-label="Microchip on a single layered circuit board" style="background:linear-gradient(135deg,#4f8a3c,#2b2f2e 45%,#6b8e55 75%,#c4a84a)"></div></div>
    <div class="abs thumb" style="left:220px;top:6px;width:202px;height:92px"><div role="img" aria-label="Double and multi layered circuit board" style="background:linear-gradient(135deg,#2f6b45,#4f9a66 50%,#1f4d34)"></div></div>
    <div class="abs product-title" style="left:6px;top:112px">Singal layered printed circuit board</div>
    <p class="abs copy" style="left:6px;top:130px;width:205px">Lorem Ipsum is simply dummy text of the printing and typesetting industry standard dummy text.</p>
    <div class="abs product-title" style="left:216px;top:112px">Double &amp; Multi layered printed circuit board</div>
    <p class="abs copy" style="left:216px;top:130px;width:205px">Lorem Ipsum is simply dummy text of the printing and typesetting industry standard dummy text.</p>
  </div>

  <h2 class="abs" style="left:95px;top:846px">Our Client</h2>
  <div class="abs clients">
    <div class="abs client" style="left:12px;color:#222">Norvessa</div>
    <div class="abs client" style="left:92px;color:#2e8a3e">Kelvoran</div>
    <div class="abs client" style="left:175px;color:#222">Marquint</div>
    <div class="abs client" style="left:262px;color:#222">Aldrevon</div>
    <div class="abs client" style="left:346px;color:#d42a1c">Vantrelo</div>
  </div>
</main>

<aside>
  <div class="abs side-head green" style="top:328px">Technical capability</div>
  <div class="abs side-body" style="top:355px;height:171px">
    <ul class="cap-list">
      <li>Raw Materials</li>
      <li>Plating</li>
      <li>Printing Processes</li>
      <li>Punching And CNC Process</li>
      <li>Depth Tolerance</li>
      <li>Surface Finishing</li>
      <li>Specification for carbon</li>
    </ul>
  </div>

  <div class="abs side-head grey" style="top:540px">Client Testimonials</div>
  <div class="abs side-body" style="top:567px;height:154px">
    <div class="abs bubble">Lorem Ipsum is simply dummy text of the printing and type-setting into industry lorem ipsum has been the industry's for on standard...</div>
    <svg class="abs" style="left:18px;top:111px" width="14" height="12" viewBox="0 0 14 12"><path d="M0 0H14L3 12Z" fill="#fff"/></svg>
    <div class="abs" style="left:5px;top:130px;font-size:9.5px;color:var(--red)">Dana Whitlow</div>
  </div>

  <div class="abs side-head grey" style="top:735px">Latest Blog</div>
  <div class="abs side-body" style="top:762px;height:196px;border-bottom:0">
    <div class="abs blog-item" style="top:9px">
      <svg width="12" height="10" viewBox="0 0 12 10"><path d="M1 1H11V7H5L2 9V7H1Z" fill="#fff" stroke="#999"/></svg>
      <h4>Neque porro est ipsum quia</h4><p>Lorem Ipsum is simply dummy text of the printing and dummy text.</p>
    </div>
    <div class="abs blog-item" style="top:57px">
      <svg width="12" height="10" viewBox="0 0 12 10"><path d="M1 1H11V7H5L2 9V7H1Z" fill="#fff" stroke="#999"/></svg>
      <h4>Neque porro est ipsum quia</h4><p>Lorem Ipsum is simply dummy text of the printing and dummy text.</p>
    </div>
    <div class="abs blog-item" style="top:105px">
      <svg width="12" height="10" viewBox="0 0 12 10"><path d="M1 1H11V7H5L2 9V7H1Z" fill="#fff" stroke="#999"/></svg>
      <h4>Neque porro est ipsum quia</h4><p>Lorem Ipsum is simply dummy text of the printing and dummy text.</p>
    </div>
    <div class="abs btn-view">View All</div>
  </div>
</aside>

<footer class="abs footer">
  <h3 style="left:96px;top:22px">Contact</h3>
  <div class="abs f-col" style="left:96px;top:55px;width:160px">
    <div class="label">Hong Kong Business Office</div>
    RVT Global Limited<br>12/F Harbour Crest<br>88 Linden Avenue
    <div class="white">Email: <u>sales@rvtboards.example</u></div>
    <div class="white" style="margin-top:3px">Phone: <span class="f-phone">(852)21904468</span></div>
    <div class="white" style="margin-top:3px">Fax: <span class="f-phone">(852)21904470</span></div>
  </div>
  <div class="abs f-col" style="left:260px;top:55px;width:200px">
    <div class="label">China Factory</div>
    RVT Global (Shenvale) Limited<br>5 Qiaoxin East Road<br>210 Industrial Park<br>Meilong Town, Shenvale<br>Southland Province, China 518400
    <div class="white" style="margin-top:2px">Phone: <span class="f-phone">(86)755-21336604</span></div>
    <div class="white" style="margin-top:2px">Fax: <span class="f-phone" style="font-size:15px">(86)755-21336610</span></div>
  </div>
  <h3 style="left:486px;top:22px">Quick Links</h3>
  <ul class="abs f-links" style="left:487px;top:54px">
    <li>Home</li><li>About Us</li><li>Products</li><li>Services</li><li>Technical Capability</li><li>Infrastructure</li><li>Our Clients</li>
  </ul>
  <h3 style="left:614px;top:22px">Follow Us</h3>
  <div class="abs social" style="top:59px"><i style="background:#3b5b9a"></i>Follow on Circlebook</div>
  <div class="abs social" style="top:97px"><i style="background:#3fa6d8"></i>Quick talk on Chirper</div>
  <div class="abs social" style="top:135px"><i style="background:#2e2e2e"></i>Add with Gloop</div>
  <div class="abs copyright" style="top:202px;left:96px">© 2012 RVT Global limited | All Rights Reserved</div>
</footer>
</body>
</html>
```